MAREK DOLVANE FOR CONGRESS DISTRICT 32

I need to create a campaign flyer for my congress campaign. I am running for congress in District 32 of Texas as a republican. I am a former Olympic athlete, world champion fencer, Army veteran, Counterintelligence officer (I catch spies).
I want just my first name MAREK in big letters at the top. I want it to say MAREK and below it Republican for Congress.
www.marekforcongress.example

Industry/Entity Type

Political

Colors
EB3D1F
EC4F4E
F09395
F8D3D4
FCEDEE

Requirements
Nice to have
• Would love a catchy title for the Flyer like "Spy Catcher", "Olympic Athlete" "World Champion Fencer" running for Congress in your District!

```html
<!DOCTYPE html>
<html lang="en">
<head>
<meta charset="utf-8">
<title>Marek Dolvane for Congress – Flyer</title>
<link href="https://fonts.googleapis.com/css2?family=Montserrat:wght@900&family=Oswald:wght@600&family=Poppins:wght@500;700;800&display=swap" rel="stylesheet">
<style>
  :root {
    --red: #EB3D1F;
    --red-soft: #EC4F4E;
    --pink: #F09395;
    --blush: #F8D3D4;
    --mist: #FCEDEE;
    --navy: #2A2F7C;
    --white: #ffffff;
    --page: #ffffff;
  }
  * { box-sizing: border-box; margin: 0; padding: 0; }
  html, body { width: 1200px; height: 680px; overflow: hidden; background: var(--page); }
  .canvas { position: relative; width: 1200px; height: 680px; }

  .flyer {
    position: absolute; left: 352px; top: 19px;
    width: 496px; height: 642px;
    background: var(--white); overflow: hidden;
    box-shadow: 0 0 0 1px #eee;
  }
  .flyer-art { position: absolute; inset: 0; }

  .brand {
    position: absolute; top: 32px; left: 0; width: 100%;
    display: flex; justify-content: center; align-items: center; gap: 6px;
    font-family: "Poppins", sans-serif; font-weight: 800; font-size: 15px;
    color: var(--red); letter-spacing: 0.2px;
  }
  .brand-mark { width: 11px; height: 11px; background: var(--navy); }

  .running-line {
    position: absolute; top: 64px; left: 0; width: 100%; text-align: center;
    font-family: "Oswald", sans-serif; font-weight: 600; font-size: 14.5px;
    color: var(--navy); text-transform: uppercase;
  }
  .running-line .accent { color: var(--red); }

  .credentials {
    position: absolute; top: 92px; left: 0; width: 100%; text-align: center;
    font-family: "Poppins", sans-serif; font-weight: 700; font-size: 18.5px;
    line-height: 24px; color: var(--navy);
  }

  .first-name {
    position: absolute; top: 176px; left: 28px;
    font-family: "Montserrat", sans-serif; font-weight: 900; font-size: 64px;
    line-height: 1; letter-spacing: -1px; color: var(--red);
    text-shadow: 2px 2px 0 var(--navy), 3px 3px 0 var(--navy);
  }
  .first-name-fade {
    position: absolute; top: 240px; left: 28px; width: 250px; height: 32px;
    background: linear-gradient(to bottom, var(--blush), rgba(255,255,255,0));
    opacity: 0.8;
  }

  .party-title {
    position: absolute; top: 284px; left: 32px;
    font-family: "Poppins", sans-serif; font-weight: 700; font-size: 25px;
    line-height: 29px; text-transform: uppercase; color: var(--navy);
  }
  .party-title .for { display: block; padding-left: 46px; }
  .party-title .congress { display: block; color: var(--red); }

  .website {
    position: absolute; left: 34px; top: 572px; height: 36px;
    border-radius: 18px; background: var(--red);
    box-shadow: 0 0 0 3px var(--white), 0 0 0 4px var(--blush);
    display: flex; align-items: center; gap: 9px; padding: 0 16px 0 10px;
    font-family: "Poppins", sans-serif; font-weight: 500; font-size: 14px; color: var(--white);
    white-space: nowrap;
  }
  .website svg { width: 20px; height: 20px; flex: none; }
</style>
</head>
<body>
<div class="canvas">
  <section class="flyer">
    <svg class="flyer-art" width="496" height="642" viewBox="0 0 496 642">
      <defs>
        <linearGradient id="portraitTone" x1="0" y1="0" x2="0" y2="1">
          <stop offset="0" stop-color="#5a4536"/>
          <stop offset="0.12" stop-color="#e7b8a2"/>
          <stop offset="0.5" stop-color="#f3d6c8"/>
          <stop offset="0.62" stop-color="#f6f3f1"/>
          <stop offset="1" stop-color="#eceae8"/>
        </linearGradient>
        <linearGradient id="uniformTone" x1="0" y1="0" x2="0" y2="1">
          <stop offset="0" stop-color="#8a8d96"/>
          <stop offset="0.5" stop-color="#c9a690"/>
          <stop offset="1" stop-color="#6f7258"/>
        </linearGradient>
        <linearGradient id="fencingTone" x1="0" y1="0" x2="1" y2="1">
          <stop offset="0" stop-color="#c26a1e"/>
          <stop offset="0.6" stop-color="#e3ddd8"/>
          <stop offset="1" stop-color="#f4f2f0"/>
        </linearGradient>
      </defs>

      <circle class="accent-arc" cx="474" cy="574" r="304" fill="none" stroke="var(--red)" stroke-width="11"/>

      <path class="portrait-main" role="img" aria-label="Photo of the candidate smiling, in a white shirt"
            d="M280 642 L276 300 C272 200 298 160 366 152 C424 146 462 180 472 230 L496 300 L496 642 Z"
            fill="url(#portraitTone)"/>

      <g class="feature-photo">
        <circle cx="99" cy="468" r="63" fill="url(#uniformTone)" role="img" aria-label="Photo of the candidate in Army uniform"/>
        <circle cx="99" cy="468" r="63" fill="none" stroke="var(--red)" stroke-width="5"/>
      </g>
      <g class="feature-photo">
        <circle cx="238" cy="468" r="63" fill="url(#fencingTone)" role="img" aria-label="Photo of the candidate fencing in competition"/>
        <circle cx="238" cy="468" r="63" fill="none" stroke="var(--red)" stroke-width="5"/>
      </g>
    </svg>

    <div class="brand"><span>MAREK DOLVANE</span><span class="brand-mark"></span></div>

    <p class="running-line"><span class="accent">Running for Congress</span> in District 32 of Texas as a Republican</p>

    <p class="credentials">Olympic athlete, world champion fencer,<br>Army veteran, Counterintelligence officer</p>

    <div class="first-name-fade"></div>
    <h1 class="first-name">MAREK</h1>

    <h2 class="party-title">Republican<span class="for">for</span><span class="congress">Congress</span></h2>

    <div class="website">
      <svg viewBox="0 0 20 20" aria-hidden="true">
        <circle cx="10" cy="10" r="9" fill="var(--white)"/>
        <g fill="none" stroke="var(--red)" stroke-width="1.2">
          <circle cx="10" cy="10" r="6.5"/>
          <ellipse cx="10" cy="10" rx="3" ry="6.5"/>
          <line x1="3.5" y1="10" x2="16.5" y2="10"/>
          <line x1="4.5" y1="6.8" x2="15.5" y2="6.8"/>
          <line x1="4.5" y1="13.2" x2="15.5" y2="13.2"/>
        </g>
      </svg>
      <span>www.marekforcongress.example</span>
    </div>
  </section>
</div>
</body>
</html>
```